Contemporary Media Company with Logo Needs Business Card Design

Need a modern card design for a full service digital media company using the logo included. Also want the info below on the card. Probably list the services on the card back to save space for the front. Want something contemporary to impress prospective clients. You may want to submit both a somewhat more conservative design, and then a more wild one.
General Info: (this phrase need not be on the card)
Tod Parvin
Founder and CEO
949-628-4513
tod@lumavantstudio.example
lumavantstudio.example
Services: (this word need not be on the card)
Content & Experience Strategy
Brand Development
Search Engine Optimization
Website Design
Website Operation
Social Media Integration
Complete Video Solutions
Industry/Entity Type
Business
Contact Information for Business Card
Tod Parvin
Founder and CEO
949-628-4513
tod@lumavantstudio.example
lumavantstudio.example
Brand Development
Website Design
Website Operation
Social Media Integration
Complete Video Solutions
Look and feel

```html
<!DOCTYPE html>
<html lang="en">
<head>
<meta charset="utf-8">
<title>Lumavant Studio – Business Card</title>
<link href="https://fonts.googleapis.com/css2?family=Source+Sans+3:wght@400;600;700&display=swap" rel="stylesheet">
<style>
  :root {
    --page-bg: #ecebe8;
    --card-white: #ffffff;
    --card-charcoal: #545454;
    --ink-dark: #4a4a4a;
    --ink-body: #5a5a5a;
    --ink-light: #f2f2f2;
    --accent-orange: #e8732a;
    --accent-soft: #f28c38;
  }
  * { box-sizing: border-box; margin: 0; padding: 0; }
  html, body {
    width: 1200px; height: 1000px; overflow: hidden;
    background: var(--page-bg);
    font-family: "Source Sans 3", "Helvetica Neue", Arial, sans-serif;
  }
  .canvas { position: relative; width: 1200px; height: 1000px; }

  .card {
    position: absolute; left: 265px; width: 666px; height: 397px; overflow: hidden;
  }
  .card--front { top: 73px; background: var(--card-white); }
  .card--back  { top: 532px; background: var(--card-charcoal); }

  /* Front */
  .brand-name {
    position: absolute; left: 34px; top: 44px;
    font-size: 44px; font-weight: 400; letter-spacing: 2px;
    line-height: 1; color: var(--ink-dark); text-transform: uppercase;
  }
  .contact-person { position: absolute; left: 65px; top: 176px; }
  .person-name { font-size: 25px; font-weight: 700; color: var(--ink-dark); line-height: 1.1; }
  .person-title { font-size: 17px; color: var(--accent-orange); margin-top: 4px; }

  .address {
    position: absolute; left: 63px; top: 248px;
    font-size: 17px; line-height: 24px; color: var(--ink-body);
  }
  .contact-list {
    position: absolute; left: 63px; top: 302px; list-style: none;
    font-size: 17px; line-height: 23px; color: var(--ink-body);
  }
  .contact-list li { display: flex; align-items: center; gap: 8px; height: 23px; }
  .contact-icon { width: 14px; height: 14px; fill: var(--accent-orange); flex: none; }

  .accent-block {
    position: absolute; background: var(--accent-soft);
  }
  .card--front .accent-block { left: 400px; top: 110px; width: 190px; height: 190px; }

  /* Back */
  .card--back .accent-block { left: 70px; top: 70px; width: 250px; height: 250px; }
  .service-list {
    position: absolute; left: 383px; top: 96px; list-style: none;
    font-size: 18px; line-height: 29px; color: var(--ink-light);
  }
  .service-list li::before { content: "- "; color: var(--accent-orange); }
</style>
</head>
<body>
<main class="canvas">

  <section class="card card--front" aria-label="Business card front">
    <div class="brand-name">Lumavant Studio</div>

    <div class="contact-person">
      <div class="person-name">Tod Parvin</div>
      <div class="person-title">Founder / CEO</div>
    </div>

    <address class="address" style="font-style:normal">
      Veldhoflaan 27A<br>1083 RT Amsterdam
    </address>

    <ul class="contact-list">
      <li>
        <svg class="contact-icon" viewBox="0 0 16 16" aria-hidden="true"><path d="M3.6 1.2l2.3 2.6c.3.4.3.9 0 1.3L4.8 6.4c.9 1.9 2.9 3.9 4.8 4.8l1.3-1.1c.4-.3.9-.3 1.3 0l2.6 2.3c.4.4.4 1 0 1.4l-1.2 1.2C11.2 16.4 0 5.2 1.6 2.4L2.2 1.2c.4-.4 1-.4 1.4 0z"/></svg>
        949-628-4513
      </li>
      <li>
        <svg class="contact-icon" viewBox="0 0 16 16" aria-hidden="true"><path d="M1 3h14v10H1z" /><path d="M1.5 3.5L8 9l6.5-5.5" stroke="#fff" stroke-width="1.4" fill="none"/></svg>
        tod@lumavantstudio.example
      </li>
      <li>
        <svg class="contact-icon" viewBox="0 0 16 16" aria-hidden="true"><circle cx="8" cy="8" r="7"/><path d="M1 8h14M8 1c-3 3.5-3 10.5 0 14M8 1c3 3.5 3 10.5 0 14" stroke="#fff" stroke-width="1.2" fill="none"/></svg>
        lumavantstudio.example
      </li>
    </ul>

    <div class="accent-block" aria-hidden="true"></div>
  </section>

  <section class="card card--back" aria-label="Business card back">
    <div class="accent-block" aria-hidden="true"></div>
    <ul class="service-list">
      <li>Content &amp; Experience Strategy</li>
      <li>Brand Development</li>
      <li>Search Engine Optimization</li>
      <li>Website Design</li>
      <li>Website Operation</li>
      <li>Social Media Integration</li>
      <li>Complete Video Solutions</li>
    </ul>
  </section>

</main>
</body>
</html>
```